Copperleaf Motorized Shade Business Card

Hello, we've had our logo made. Now we are looking for a clean and cool looking business card. One side can just be the logo with any design elements that might look good with it. The other side will be Name, Phone Number and Email. There will not be an address on the card.

```html
<!DOCTYPE html>
<html lang="en">
<head>
<meta charset="utf-8">
<title>Copperleaf Motorized Shade – Business Card</title>
<link rel="stylesheet" href="https://fonts.googleapis.com/css2?family=Oswald:wght@600&family=Montserrat:wght@500&display=swap">
<style>
  :root {
    --navy: #173a6e;
    --sky: #2aa3e0;
    --sun: #f5b81c;
    --paper: #ffffff;
    --backdrop: #eef1f4;
    --ink: #1c3a6b;
  }
  * { margin: 0; padding: 0; box-sizing: border-box; }
  html, body { width: 1200px; height: 1000px; overflow: hidden; }
  body {
    background: var(--backdrop);
    position: relative;
    font-family: "Montserrat", sans-serif;
  }
  .card {
    position: absolute;
    left: 320px;
    width: 560px;
    height: 320px;
    box-shadow: 0 6px 18px rgba(0, 0, 0, 0.12);
  }
  .card--front { top: 150px; background: var(--paper); }
  .card--back { top: 530px; background: var(--navy); }

  /* Front side */
  .identity {
    position: absolute;
    left: 44px;
    top: 92px;
    display: flex;
    align-items: flex-start;
    gap: 16px;
  }
  .identity__mark {
    width: 26px;
    height: 26px;
    margin-top: 6px;
    background: var(--sun);
  }
  .identity__name {
    font-family: "Oswald", sans-serif;
    font-weight: 600;
    font-size: 34px;
    line-height: 1.1;
    color: var(--navy);
    letter-spacing: 0.5px;
    text-transform: uppercase;
  }
  .identity__role {
    font-family: "Oswald", sans-serif;
    font-weight: 600;
    font-size: 20px;
    color: var(--navy);
    text-transform: uppercase;
    margin-top: 2px;
  }
  .contact-rule {
    position: absolute;
    left: 240px;
    right: 0;
    top: 206px;
    height: 1px;
    background: var(--sky);
  }
  .contact {
    position: absolute;
    left: 240px;
    top: 218px;
    list-style: none;
    font-size: 12px;
    line-height: 1.55;
    color: var(--ink);
    letter-spacing: 0.4px;
    white-space: nowrap;
  }

  /* Back side */
  .brand {
    position: absolute;
    inset: 0;
    display: flex;
    align-items: center;
    justify-content: center;
    gap: 14px;
  }
  .brand__mark {
    width: 30px;
    height: 30px;
    background: var(--sun);
  }
  .brand__name {
    font-family: "Oswald", sans-serif;
    font-weight: 600;
    font-size: 32px;
    color: var(--paper);
    letter-spacing: 1px;
    text-transform: uppercase;
  }
</style>
</head>
<body>
  <section class="card card--front" aria-label="Business card, contact side">
    <div class="identity">
      <span class="identity__mark" aria-hidden="true"></span>
      <div>
        <p class="identity__name">Daniel Marsh</p>
        <p class="identity__role">CEO</p>
      </div>
    </div>
    <div class="contact-rule" aria-hidden="true"></div>
    <ul class="contact">
      <li>E: danielmarsh@copperleafshade.com</li>
      <li>C: (044) 55 3170-2648</li>
      <li>O: (55) 5281-4907</li>
    </ul>
  </section>

  <section class="card card--back" aria-label="Business card, brand side">
    <div class="brand">
      <span class="brand__mark" aria-hidden="true"></span>
      <p class="brand__name">Copperleaf Motorized Shade</p>
    </div>
  </section>
</body>
</html>
```